Brovan Equipment Sales & Rentals

We are an independent equipment dealership located in the upstate of South Carolina. Our services include Equipment Sales, Equipment Rentals, Metal Sales, and Industrial Supplies.

I have attached our logos and a few billboards that we like as examples for inspiration. Thank you!

Phone Number 864-555-0172

Website link if you want to check out our page.
https://www.brovanmachinery.example

```html
<!DOCTYPE html>
<html lang="en">
<head>
<meta charset="utf-8">
<title>Brovan Equipment Sales &amp; Rentals — Billboard</title>
<link href="https://fonts.googleapis.com/css2?family=Barlow:ital,wght@0,400;0,500;0,600;1,500&family=Barlow+Semi+Condensed:wght@700&display=swap" rel="stylesheet">
<style>
  :root {
    --brand-red: #f2302a;
    --ink: #23252b;
    --white: #ffffff;
    --stage: #707070;
    --sky: #9dbde0;
    --hills: #4f7a3c;
    --ground: #a88b68;
  }
  html, body {
    margin: 0;
    width: 943px;
    height: 1200px;
    overflow: hidden;
    background: var(--stage);
  }
  .stage {
    width: 943px;
    height: 1200px;
    display: flex;
    align-items: center;
    justify-content: center;
  }
  .billboard {
    width: 863px;
    height: 431px;
    box-shadow: 0 8px 14px rgba(0,0,0,0.45);
  }
  .billboard svg { display: block; width: 100%; height: 100%; }
  .headline { font-family: "Barlow Semi Condensed", "Arial Narrow", sans-serif; font-weight: 700; font-size: 64px; fill: var(--brand-red); }
  .tagline { font-family: "Barlow", Arial, sans-serif; font-style: italic; font-weight: 500; font-size: 35px; fill: var(--ink); }
  .tab-label { font-family: "Barlow", Arial, sans-serif; font-weight: 500; font-size: 37px; fill: var(--white); }
  .service { font-family: "Barlow", Arial, sans-serif; font-weight: 500; font-size: 29px; fill: var(--white); }
  .phone-number { font-family: "Barlow Semi Condensed", "Arial Narrow", sans-serif; font-weight: 700; font-size: 92px; fill: var(--white); }
  .web-address { font-family: "Barlow", Arial, sans-serif; font-weight: 600; font-size: 33px; letter-spacing: 3px; fill: var(--ink); }
  .brand-name { font-family: "Barlow Semi Condensed", "Arial Narrow", sans-serif; font-weight: 700; font-size: 82px; fill: var(--ink); }
  .icon-line { fill: none; stroke: var(--white); stroke-width: 2.5; }
</style>
</head>
<body>
<main class="stage">
  <section class="billboard" aria-label="Brovan Equipment Sales &amp; Rentals billboard">
    <svg viewBox="0 0 1526 762" xmlns="http://www.w3.org/2000/svg">
      <defs>
        <linearGradient id="site-photo-tones" x1="0" y1="0" x2="0" y2="1">
          <stop offset="0" stop-color="var(--sky)"/>
          <stop offset="0.38" stop-color="#c6d6e6"/>
          <stop offset="0.52" stop-color="var(--hills)"/>
          <stop offset="0.78" stop-color="#5f7f48"/>
          <stop offset="1" stop-color="var(--ground)"/>
        </linearGradient>
      </defs>

      <rect class="canvas-base" width="1526" height="762" fill="var(--white)"/>

      <g class="hero-photo" role="img" aria-label="Photo of an orange and a yellow excavator on a dirt work site with green hills and blue sky behind">
        <polygon points="811,0 1526,0 1526,762 905,762 887,715 909,637 855,637 728,300" fill="url(#site-photo-tones)"/>
      </g>

      <polygon class="services-panel" points="0,300 728,300 855,637 0,637" fill="var(--brand-red)"/>
      <polygon class="web-band" points="0,637 909,637 887,715 0,715" fill="var(--white)"/>
      <polygon class="footer-strip" points="0,715 887,715 905,762 0,762" fill="var(--brand-red)"/>

      <text class="headline" x="48" y="113">INDEPENDENT EQUIPMENT</text>
      <text class="headline" x="48" y="183">DEALERSHIP</text>
      <text class="tagline" x="50" y="226">Located in the upstate of South Carolina.</text>

      <polygon class="services-tab" points="62,272 339,272 326,330 49,330" fill="var(--ink)"/>
      <text class="tab-label" x="90" y="313">Our services</text>

      <g class="service-icon" role="img" aria-label="Excavator icon">
        <rect class="icon-line" x="48" y="360" width="52" height="48" rx="6"/>
      </g>
      <text class="service" x="131" y="382">Equipment</text>
      <text class="service" x="131" y="417">Sales</text>

      <g class="service-icon" role="img" aria-label="Metal stock icon">
        <rect class="icon-line" x="48" y="444" width="52" height="48" rx="6"/>
      </g>
      <text class="service" x="131" y="466">Metal</text>
      <text class="service" x="131" y="499">Sales</text>

      <line class="services-divider" x1="358" y1="357" x2="358" y2="495" stroke="var(--white)" stroke-width="2.5"/>

      <g class="service-icon" role="img" aria-label="Rental machine icon">
        <rect class="icon-line" x="431" y="360" width="52" height="48" rx="6"/>
      </g>
      <text class="service" x="513" y="382">Equipment</text>
      <text class="service" x="513" y="417">Rentals</text>

      <g class="service-icon" role="img" aria-label="Industrial plant icon">
        <rect class="icon-line" x="431" y="444" width="52" height="48" rx="6"/>
      </g>
      <text class="service" x="513" y="466">Industrial</text>
      <text class="service" x="513" y="499">Supplies</text>

      <rect class="phone-frame" x="47" y="522" width="729" height="95" fill="none" stroke="var(--white)" stroke-width="2.5"/>
      <g class="phone-icon" fill="var(--white)">
        <path d="M92 548c6-5 12-4 15 2l7 13c2 5 0 9-4 11l-5 3c3 8 9 15 17 19l3-5c3-4 7-5 11-3l12 8c5 3 6 9 1 14l-6 6c-6 5-16 5-26-1-17-10-29-26-33-44-2-9 0-16 5-20z"/>
        <path d="M118 545a26 26 0 0 1 26 26" fill="none" stroke="var(--white)" stroke-width="5" stroke-linecap="round"/>
        <path d="M118 532a39 39 0 0 1 39 39" fill="none" stroke="var(--white)" stroke-width="5" stroke-linecap="round"/>
      </g>
      <text class="phone-number" x="173" y="602">864-555-0172</text>

      <g class="globe-icon" fill="none" stroke="var(--brand-red)" stroke-width="4">
        <circle cx="104" cy="677" r="24" fill="var(--brand-red)"/>
        <ellipse cx="104" cy="677" rx="10" ry="24" stroke="var(--white)" stroke-width="3"/>
        <line x1="80" y1="669" x2="128" y2="669" stroke="var(--white)" stroke-width="3"/>
        <line x1="80" y1="685" x2="128" y2="685" stroke="var(--white)" stroke-width="3"/>
      </g>
      <text class="web-address" x="160" y="690">WWW.BROVANMACHINERY.EXAMPLE</text>

      <g class="brand-lockup">
        <rect x="1128" y="53" width="52" height="52" fill="var(--brand-red)"/>
        <text class="brand-name" x="1196" y="106">BROVAN</text>
      </g>
    </svg>
  </section>
</main>
</body>
</html>
```